Flyer Template

I need a flyer template for door knocking on properties. Text Boxes need to be editable, with a header and text body. Footer to be my info. Project to be stylized to match my real estate signs and logo art from past projects

```html
<!DOCTYPE html>
<html lang="en">
<head>
<meta charset="utf-8">
<title>Brennan Realty – Door Knocking Flyer</title>
<link href="https://fonts.googleapis.com/css2?family=Montserrat:wght@500;600;700;800&family=Open+Sans:wght@400;600&display=swap" rel="stylesheet">
<style>
  :root{
    --brand-red:#e3192b;
    --brand-red-dark:#c8101f;
    --ink:#2b2b2b;
    --muted:#6d6d6d;
    --paper:#ffffff;
    --backdrop:#d9d9d9;
    --sky-top:#a9c4dc;
    --sky-bottom:#e6eef5;
    --lawn:#7f9a52;
  }
  *{margin:0;padding:0;box-sizing:border-box}
  html,body{width:748px;height:1200px;overflow:hidden;background:var(--backdrop)}
  body{font-family:"Open Sans",Arial,sans-serif;color:var(--ink);position:relative}
  .flyer{position:absolute;left:20px;top:100px;width:708px;height:1000px;background:var(--paper);overflow:hidden;box-shadow:0 6px 18px rgba(0,0,0,.18)}
  .hero-photo{position:absolute;left:0;top:130px;width:708px;height:380px;
    background:linear-gradient(180deg,var(--sky-top) 0%,var(--sky-bottom) 45%,#cfcfcf 46%,#8d8d8d 72%,var(--lawn) 73%,#5f7a3a 100%)}
  .brand-panel{position:absolute;left:0;top:0;width:270px;height:240px;background:var(--brand-red);
    display:flex;align-items:center;justify-content:center;padding:0 24px}
  .brand-name{font-family:"Montserrat",Arial,sans-serif;font-weight:800;color:#fff;font-size:34px;line-height:1.05;letter-spacing:.5px;text-transform:uppercase;text-align:center}
  .offer{position:absolute;left:300px;top:26px;width:380px;border-left:2px solid var(--brand-red);padding-left:16px}
  .offer-label{font-family:"Montserrat",Arial,sans-serif;font-weight:700;font-size:14px;letter-spacing:1px;color:var(--ink)}
  .offer-price{font-family:"Montserrat",Arial,sans-serif;font-weight:600;font-size:40px;color:var(--brand-red);line-height:1.1}
  .offer-price sup{font-size:18px;vertical-align:top;position:relative;top:6px;margin-right:2px}
  .offer-text{font-size:11px;color:var(--brand-red);line-height:1.45;margin-top:4px;width:260px}
  .about-panel{position:absolute;left:0;top:510px;width:270px;height:490px;background:var(--brand-red);color:#fff;padding:34px 26px}
  .about-title{font-family:"Montserrat",Arial,sans-serif;font-weight:600;font-size:40px;line-height:1;margin-bottom:18px}
  .about-text{font-size:11.5px;line-height:1.55;margin-bottom:14px}
  .agent{position:absolute;left:26px;bottom:40px}
  .agent-name{font-family:"Montserrat",Arial,sans-serif;font-weight:700;font-size:20px;letter-spacing:.5px}
  .agent-line{display:flex;align-items:center;gap:8px;font-family:"Montserrat",Arial,sans-serif;font-weight:700}
  .agent-phone{font-size:26px;line-height:1.2}
  .agent-web{font-size:12px;letter-spacing:.5px;margin-top:4px}
  .rooms{position:absolute;left:296px;top:540px;width:390px;display:grid;grid-template-columns:repeat(3,1fr);gap:14px}
  .room-photo{height:96px;background:linear-gradient(160deg,#e9e4dc,#9a8f80 70%,#5e554b)}
  .room:nth-child(2) .room-photo{background:linear-gradient(160deg,#f1eee9,#b4a795 60%,#6c6256)}
  .room:nth-child(3) .room-photo{background:linear-gradient(160deg,#f4f2ee,#c9c1b5 60%,#847a6d)}
  .room-title{font-family:"Montserrat",Arial,sans-serif;font-weight:700;font-size:11px;color:var(--brand-red);margin:10px 0 4px}
  .room-text{font-size:9.5px;color:var(--muted);line-height:1.45}
  .body-copy{position:absolute;left:296px;top:745px;width:390px;font-size:11.5px;line-height:1.55;color:var(--ink)}
  .body-copy p+p{margin-top:10px}
  .partner{position:absolute;left:296px;top:900px;width:390px;display:flex;align-items:center;justify-content:space-between}
  .partner-name{font-family:"Montserrat",Arial,sans-serif;font-weight:700;font-size:20px;color:var(--ink);text-transform:uppercase;letter-spacing:.5px}
  .partner-note{font-size:8.5px;color:var(--muted);width:140px;text-align:right;line-height:1.4;border-left:1px solid #ccc;padding-left:10px}
</style>
</head>
<body>
<main class="flyer">
  <div class="hero-photo" role="img" aria-label="Photo of a modern two-storey family home with grey roof and front lawn"></div>

  <header class="brand-panel">
    <div class="brand-name">Brennan<br>Realty</div>
  </header>

  <section class="offer">
    <div class="offer-label">OFFERS AT</div>
    <div class="offer-price"><sup>$</sup>3,00,000</div>
    <p class="offer-text">A bright family home on a quiet street, ready for its next owners.</p>
  </section>

  <aside class="about-panel">
    <h2 class="about-title">About US:</h2>
    <p class="about-text">We have helped local families buy and sell homes for over a decade, with honest advice at every step.</p>
    <p class="about-text">If you are thinking of selling this season, call us for a free and friendly market review.</p>
    <div class="agent">
      <div class="agent-name">JORDAN BRENNAN</div>
      <div class="agent-line agent-phone">
        <svg width="20" height="20" viewBox="0 0 24 24" aria-hidden="true"><path fill="#fff" d="M6.6 10.8a15.1 15.1 0 0 0 6.6 6.6l2.2-2.2a1 1 0 0 1 1-.25 11.4 11.4 0 0 0 3.6.57 1 1 0 0 1 1 1V20a1 1 0 0 1-1 1A17 17 0 0 1 3 4a1 1 0 0 1 1-1h3.5a1 1 0 0 1 1 1c0 1.25.2 2.45.57 3.6a1 1 0 0 1-.25 1z"/></svg>
        555-014-0288
      </div>
      <div class="agent-line agent-web">
        <svg width="12" height="12" viewBox="0 0 12 12" aria-hidden="true"><path d="M3 2l5 4-5 4z" fill="#fff"/></svg>
        BRENNANREALTY.EXAMPLE
      </div>
    </div>
  </aside>

  <section class="rooms">
    <article class="room">
      <div class="room-photo" role="img" aria-label="Photo of the living room"></div>
      <h3 class="room-title">LIVING ROOM</h3>
      <p class="room-text">Open plan space with large windows and warm oak floors.</p>
    </article>
    <article class="room">
      <div class="room-photo" role="img" aria-label="Photo of the dining room"></div>
      <h3 class="room-title">DINING ROOM</h3>
      <p class="room-text">Seats eight with easy access to the kitchen and deck.</p>
    </article>
    <article class="room">
      <div class="room-photo" role="img" aria-label="Photo of the bedroom"></div>
      <h3 class="room-title">BED ROOM</h3>
      <p class="room-text">Calm main suite with walk-in closet and ensuite bath.</p>
    </article>
  </section>

  <section class="body-copy">
    <p>Every home on this street has its own story. Ask us how much yours could be worth today, and how quickly we can find the right buyer for it.</p>
    <p>Book a visit this week.</p>
  </section>

  <footer class="partner">
    <span class="partner-name">Northfield Group</span>
    <span class="partner-note">Each office independently owned and operated</span>
  </footer>
</main>
</body>
</html>
```